Harbor Notes

I have written a book which I eventually would like to serve a couple of purposes. The initial purpose was to memorialize life events and lessons from my life to pass on to my grandchildren, in hopes they may learn from the experiences. As I completed the book, I now believe I could remove some of the family specific information as much of the information could be useful to many people.

While I want to book to have a great look for the grandkids, more importantly will be the version that we put on the bookshelf to sell. The cover is obviously the first thing a buyer will see and may or may not peak there interest. I would like to include the attached photo as the cover photo and the title language is also attached. Other than that I am not sure what is the best way to design the cover.

```html
<!DOCTYPE html>
<html lang="en">
<head>
<meta charset="utf-8">
<title>Hi, Guys — Cover</title>
<link rel="stylesheet" href="https://fonts.googleapis.com/css2?family=Comic+Neue:wght@400;700&family=Arimo:ital,wght@1,700&display=swap">
<style>
  :root {
    --page-bg: #f4f4f2;
    --spine-orange: #f7b500;
    --accent-orange: #f8a800;
    --cover-green: #8cc63e;
    --cover-green-light: #a6d65a;
    --panel-blue: #37bdf0;
    --panel-blue-light: #6fd2f6;
    --ink: #111111;
    --white: #ffffff;
  }
  * { box-sizing: border-box; margin: 0; padding: 0; }
  html, body { width: 919px; height: 1200px; overflow: hidden; }
  body { background: var(--page-bg); position: relative; font-family: "Comic Neue", "Comic Sans MS", cursive; }

  .book { position: absolute; left: 115px; top: 70px; width: 690px; height: 1060px; display: flex; box-shadow: 0 10px 30px rgba(0,0,0,.18); }

  .spine { width: 70px; height: 100%; background: var(--spine-orange); position: relative; }
  .spine-title {
    position: absolute; left: 50%; top: 50%;
    transform: translate(-50%, -50%) rotate(-90deg);
    white-space: nowrap;
    font-family: "Arimo", Arial, sans-serif; font-style: italic; font-weight: 700;
    font-size: 25px; color: var(--ink);
  }

  .front { width: 620px; height: 100%; position: relative; background: var(--cover-green); overflow: hidden; }

  .title-band { position: absolute; left: 0; top: 0; width: 100%; height: 210px; background: var(--cover-green); }
  .title-band .block { position: absolute; background: var(--cover-green-light); }
  .block.b1 { left: 330px; top: 0; width: 120px; height: 95px; }
  .block.b2 { left: 520px; top: 110px; width: 100px; height: 100px; }
  .title { position: absolute; left: 40px; top: 26px; color: var(--white); font-weight: 700; font-size: 50px; line-height: 1.15; }

  .photo-panel { position: absolute; left: 0; top: 210px; width: 100%; height: 490px; background: linear-gradient(160deg, var(--panel-blue-light), var(--panel-blue) 55%); }
  .photo-frame {
    position: absolute; left: 28px; top: 42px; width: 560px; height: 360px;
    background: var(--white); padding: 10px; transform: rotate(-2.5deg);
    box-shadow: 0 6px 14px rgba(0,0,0,.25);
  }
  .photo { width: 100%; height: 100%; background: linear-gradient(180deg, #6b5a4a 0%, #8c7a68 40%, #b9b0a4 70%, #7a8a55 100%); }
  .names { position: absolute; left: 0; top: 412px; width: 100%; text-align: center; color: var(--white); font-weight: 700; font-size: 20px; line-height: 1.3; }

  .divider { position: absolute; left: 0; top: 700px; width: 100%; height: 22px; background: var(--accent-orange); }

  .message { position: absolute; left: 0; top: 722px; width: 100%; height: 338px; }
  .line { position: absolute; color: var(--ink); font-weight: 700; font-size: 21px; white-space: nowrap; }
  .line.l1 { left: 40px; top: 58px; }
  .line.l2 { left: 40px; top: 124px; }
  .line.l2 .life { color: var(--white); font-size: 38px; vertical-align: -4px; }
  .aside { position: absolute; left: 262px; top: 112px; color: var(--ink); font-size: 14px; font-weight: 700; white-space: nowrap; }
  .line.l3 { left: 40px; top: 192px; }
  .signature { position: absolute; left: 385px; top: 176px; color: var(--white); font-weight: 700; font-size: 24px; white-space: nowrap; }
</style>
</head>
<body>
  <div class="book">
    <div class="spine">
      <p class="spine-title">Lessons from my life to pass on to my grandchildren</p>
    </div>
    <div class="front">
      <header class="title-band">
        <span class="block b1"></span>
        <span class="block b2"></span>
        <h1 class="title">Hi,<br>Guys...............</h1>
      </header>
      <section class="photo-panel">
        <div class="photo-frame">
          <div class="photo" role="img" aria-label="Family photo of a grandfather sitting on porch steps with his seven grandsons"></div>
        </div>
        <p class="names">Owen... Lucas... Miles... Ben... Elliot... Henry...<br>Theodore</p>
      </section>
      <div class="divider"></div>
      <section class="message">
        <p class="line l1">There’s a bump in the road ahead......</p>
        <p class="line l2">It’s called <span class="life">LIFE</span></p>
        <p class="aside">(and life isn’t fair)</p>
        <p class="line l3">This is about having a great one.</p>
        <p class="signature">Grandpa Halvorsen</p>
      </section>
    </div>
  </div>
</body>
</html>
```